Graphic Icon Set of 35 Icons

We are looking for a set of 35 graphic icons that we can use in all of our materials, from our new content website (under design), our PowerPoint presentations, our white papers, etc.
We prefer thin and elegant icons, but we are open to any style a designer might come up with, including multi-color or monochromatic, etc. Simpler is better than complex. We prefer a very clean design without the "noise" of really "busy" graphics. We specifically do not want any 3D graphics or graphics with shading or shine. We prefer a flat design.
We are looking for designer submissions that show an example of just three of the graphic icons: an icon that represents "Valuation" - how to value a business, an icon that represents "Advisory" - consulting with businesses, and an icon that represents a "Survey" - a reader survey. Please submit all three design in one submission in one view to make it easier for us to sort through the submissions.
We will then pick a winner and in order to get paid the full amount, you will need to design and deliver the rest of the set of 35 icons.
We are attaching a list of the 35 graphic icons we will want to be delivered by the winner in high-res, tightly-trimmed EPS, JPEG, and PNG file formats.
We are attaching a brand guidelines PDF with the description of our fonts, colors, logo, and images. We are also attaching an EPS of our logo.

```html
<!DOCTYPE html>
<html lang="en">
<head>
<meta charset="utf-8">
<title>Business Topic Icons – App Screen</title>
<link href="https://fonts.googleapis.com/css2?family=Open+Sans:wght@400;600&display=swap" rel="stylesheet">
<style>
  :root {
    --backdrop: #8f8e8f;
    --screen: #ffffff;
    --accent: #e0552f;
    --label: #7a7a7a;
    --glyph: #ffffff;
  }
  html, body {
    margin: 0;
    width: 1200px;
    height: 900px;
    overflow: hidden;
    background: var(--backdrop);
    font-family: "Open Sans", Arial, sans-serif;
  }
  .app-screen {
    position: absolute;
    left: 410px;
    top: 90px;
    width: 380px;
    height: 720px;
    background: var(--screen);
    display: flex;
    flex-direction: column;
  }
  .icon-grid {
    flex: 1;
    display: grid;
    grid-template-columns: repeat(3, 96px);
    grid-auto-rows: 140px;
    column-gap: 28px;
    justify-content: center;
    padding-top: 40px;
  }
  .topic {
    display: flex;
    flex-direction: column;
    align-items: center;
  }
  .topic-tile {
    width: 96px;
    height: 96px;
    border-radius: 6px;
    background: var(--accent);
    display: flex;
    align-items: center;
    justify-content: center;
  }
  .topic-tile svg {
    width: 60px;
    height: 60px;
  }
  .topic-label {
    margin-top: 8px;
    font-size: 11px;
    font-weight: 400;
    line-height: 1.25;
    color: var(--label);
    text-align: center;
    white-space: nowrap;
  }
  .footer-band {
    height: 70px;
    background: var(--accent);
  }
</style>
</head>
<body>
  <main class="app-screen">
    <section class="icon-grid">
      <div class="topic">
        <div class="topic-tile">
          <svg viewBox="0 0 60 60" fill="none" stroke="#fff" stroke-width="2.5">
            <rect x="8" y="8" width="44" height="30"/>
            <polyline points="14,32 24,24 32,28 44,16"/>
            <line x1="30" y1="38" x2="20" y2="54"/><line x1="30" y1="38" x2="40" y2="54"/>
          </svg>
        </div>
        <div class="topic-label">Plan</div>
      </div>
      <div class="topic">
        <div class="topic-tile">
          <svg viewBox="0 0 60 60" fill="#fff">
            <rect x="8" y="38" width="8" height="14"/><rect x="20" y="30" width="8" height="22"/>
            <rect x="32" y="24" width="8" height="28"/><rect x="44" y="16" width="8" height="36"/>
            <polyline points="6,36 22,24 34,20 50,8" fill="none" stroke="#fff" stroke-width="3"/>
          </svg>
        </div>
        <div class="topic-label">Grow</div>
      </div>
      <div class="topic">
        <div class="topic-tile">
          <svg viewBox="0 0 60 60" fill="none" stroke="#fff" stroke-width="3">
            <rect x="8" y="10" width="44" height="40"/>
            <line x1="44" y1="30" x2="18" y2="30"/>
            <polyline points="28,20 18,30 28,40"/>
          </svg>
        </div>
        <div class="topic-label">Exit</div>
      </div>

      <div class="topic">
        <div class="topic-tile">
          <svg viewBox="0 0 60 60" fill="none" stroke="#fff" stroke-width="2.5">
            <rect x="6" y="10" width="48" height="36"/>
            <polygon points="14,40 48,14 30,44 26,34" fill="#fff"/>
          </svg>
        </div>
        <div class="topic-label">M &amp; A</div>
      </div>
      <div class="topic">
        <div class="topic-tile">
          <svg viewBox="0 0 60 60" fill="none" stroke="#fff" stroke-width="3">
            <circle cx="30" cy="32" r="14"/>
            <circle cx="30" cy="32" r="20" stroke-dasharray="5 5"/>
            <text x="30" y="38" font-size="16" font-family="Open Sans, sans-serif" text-anchor="middle" fill="#fff" stroke="none">$</text>
          </svg>
        </div>
        <div class="topic-label">Operations</div>
      </div>
      <div class="topic">
        <div class="topic-tile">
          <svg viewBox="0 0 60 60" fill="#fff">
            <rect x="8" y="40" width="10" height="12"/><rect x="22" y="34" width="10" height="18"/>
            <rect x="36" y="28" width="10" height="24"/>
            <path d="M8 34 Q30 30 46 10" fill="none" stroke="#fff" stroke-width="3"/>
            <polygon points="40,8 52,4 50,16"/>
          </svg>
        </div>
        <div class="topic-label">Profit</div>
      </div>

      <div class="topic">
        <div class="topic-tile">
          <svg viewBox="0 0 60 60" fill="none" stroke="#fff" stroke-width="2.5">
            <rect x="10" y="16" width="42" height="28"/>
            <line x1="31" y1="44" x2="31" y2="52"/><line x1="22" y1="52" x2="40" y2="52"/>
            <g fill="#fff" stroke="none">
              <rect x="20" y="32" width="4" height="8"/><rect x="27" y="26" width="4" height="14"/>
              <rect x="34" y="29" width="4" height="11"/><rect x="41" y="24" width="4" height="16"/>
            </g>
          </svg>
        </div>
        <div class="topic-label">Technology</div>
      </div>
      <div class="topic">
        <div class="topic-tile">
          <svg viewBox="0 0 60 60" fill="#fff">
            <circle cx="18" cy="38" r="11"/>
            <rect x="32" y="32" width="6" height="18"/><rect x="42" y="24" width="6" height="26"/>
            <polyline points="28,30 40,18 52,8" fill="none" stroke="#fff" stroke-width="3"/>
            <text x="18" y="44" font-size="15" font-family="Open Sans, sans-serif" font-weight="600" text-anchor="middle" fill="#e0552f">$</text>
          </svg>
        </div>
        <div class="topic-label">Valuation</div>
      </div>
      <div class="topic">
        <div class="topic-tile">
          <svg viewBox="0 0 60 60" fill="#fff" stroke="#fff" stroke-width="2.5">
            <line x1="30" y1="18" x2="16" y2="38"/><line x1="30" y1="18" x2="44" y2="38"/>
            <line x1="16" y1="38" x2="44" y2="38"/>
            <circle cx="30" cy="16" r="7"/><circle cx="16" cy="40" r="9"/><circle cx="44" cy="40" r="9"/>
          </svg>
        </div>
        <div class="topic-label">Leadership<br>and Employees</div>
      </div>

      <div class="topic">
        <div class="topic-tile">
          <svg viewBox="0 0 60 60" fill="none" stroke="#fff" stroke-width="2.5" stroke-linejoin="round">
            <path d="M6 10 H36 V30 H18 L10 37 V30 H6 Z"/>
            <path d="M42 22 H54 V42 H50 V49 L42 42 H24 V36"/>
            <line x1="12" y1="18" x2="30" y2="18"/><line x1="12" y1="23" x2="26" y2="23"/>
          </svg>
        </div>
        <div class="topic-label">Advisory</div>
      </div>
      <div class="topic">
        <div class="topic-tile">
          <svg viewBox="0 0 60 60" fill="none" stroke="#fff" stroke-width="2.5" stroke-linecap="round" stroke-linejoin="round">
            <rect x="12" y="10" width="36" height="44" rx="2"/>
            <rect x="22" y="6" width="16" height="8" rx="1" fill="#fff"/>
            <polyline points="17,24 20,27 25,21"/><line x1="29" y1="24" x2="42" y2="24"/>
            <polyline points="17,34 20,37 25,31"/><line x1="29" y1="34" x2="42" y2="34"/>
            <polyline points="17,44 20,47 25,41"/><line x1="29" y1="44" x2="42" y2="44"/>
          </svg>
        </div>
        <div class="topic-label">Survey</div>
      </div>
    </section>
    <footer class="footer-band"></footer>
  </main>
</body>
</html>
```